Chocolate bar label - qu4cocoa MT#3

This is a new SKU for a new product line. This is a limited edition SKU, art/design should pop, be bold and striking. The main image will be flaming heart in a tattoo style. If it works in; we want to incorporate cocoa flowers, and two scroll banners with the name of the product (e.g., qu4cocoa, Moon Tonic Batch 3. Fonts are your choice and can be an appropriate font for a heart tattoo of this style. I attached some heart (tat) examples, they all look great in their own right, so the design style and background colors, etc. is your choice. Additionally, we were thinking chocolate dripping from the bottom of the heart might be cool. <br/>Also attaching existing SKUs and POS box for reference.
Target Market(s)
Anyone who loves chocolate
Colors
Designer to choose colors to be used in the design.
Requirements
Must have
- Must pop on the shelf, need the bleeding heart tattoo graphic as described with a corresponding background color.
- Consider the complete front panel your canvas.
- Adobe vector file that we can work with to complete.
- I can send you formatted template if you want.
- Call or email if you have questions.
Nice to have
- A banging bleeding heart design in a tat style with a cool background
Should not have
- Not needing the back panel on the right side or the bottom in the attached images of existing SKUs.

```html
<!DOCTYPE html>
<html lang="en">
<head>
<meta charset="utf-8">
<title>qu4cocoa – Moon Tonic Batch 3 label</title>
<link rel="stylesheet" href="https://fonts.googleapis.com/css2?family=Archivo+Black&family=Cabin+Condensed:wght@500;600&family=Roboto:wght@400;500&family=Yellowtail&display=block">
<style>
  :root {
    --page: #ffffff;
    --sand: #d3c69c;
    --cream: #e4e6d6;
    --cocoa: #6a3a2a;
    --leaf: #3e9a3a;
    --red: #981b1e;
    --red-deep: #7a1114;
    --silver: #c6c7cb;
    --silver-dark: #a3a2a6;
    --white: #ffffff;
    --guide: #9a9a9a;
  }
  * { box-sizing: border-box; margin: 0; padding: 0; }
  html, body { width: 1200px; height: 1000px; overflow: hidden; background: var(--page); }
  .label {
    position: absolute; left: 337px; top: 40px;
    width: 491px; height: 905px; overflow: hidden;
    font-family: "Roboto", sans-serif;
  }
  .band-top { position: absolute; left: 0; top: 0; width: 100%; height: 305px; background: var(--sand); }
  .band-mid { position: absolute; left: 0; top: 305px; width: 100%; height: 295px; background: var(--cream); }
  .band-low { position: absolute; left: 0; top: 600px; width: 100%; height: 305px;
    background: linear-gradient(180deg, var(--red) 0%, var(--red-deep) 140%); }
  .trim-guide { position: absolute; left: 54px; top: 17px; width: 384px; height: 868px;
    border: 1.5px dashed var(--guide); pointer-events: none; }

  .wordmark { position: absolute; right: 53px; top: 34px;
    font-family: "Cabin Condensed", sans-serif; font-weight: 600; font-size: 94px;
    line-height: 1; color: var(--cocoa); letter-spacing: -1px; }
  .product-name { position: absolute; right: 55px; top: 136px;
    font-family: "Cabin Condensed", sans-serif; font-weight: 500; font-size: 32px;
    color: var(--cocoa); line-height: 1; }
  .maker { position: absolute; right: 66px; top: 214px;
    font-family: "Cabin Condensed", sans-serif; font-weight: 500; font-size: 22px;
    color: var(--leaf); line-height: 1; }

  .hero-art { position: absolute; left: 57px; top: 281px; width: 377px; height: 330px;
    border-radius: 38% 38% 30% 30% / 34% 34% 26% 26%;
    background:
      radial-gradient(ellipse 46% 24% at 50% 44%, var(--silver) 0%, var(--silver) 55%, rgba(198,199,203,0) 100%),
      radial-gradient(ellipse 60% 14% at 50% 64%, var(--silver-dark) 0%, rgba(163,162,166,0) 100%),
      linear-gradient(180deg, var(--red) 0%, #a01d21 50%, var(--red) 100%); }

  .crafted { position: absolute; left: 0; top: 604px; width: 100%; height: 36px; text-align: center; }
  .crafted-word { font-family: "Yellowtail", "Brush Script MT", cursive; font-size: 33px;
    color: var(--white); line-height: 36px; }
  .crafted-rule { position: absolute; top: 18px; height: 2px; background: var(--white); width: 82px; }
  .crafted-rule.left { left: 73px; }
  .crafted-rule.right { right: 68px; }

  .descriptor { position: absolute; left: 0; top: 641px; width: 100%; text-align: center;
    color: var(--white); font-size: 26.5px; line-height: 27px; }

  .stats { position: absolute; left: 62px; top: 694px; width: 372px; height: 74px; display: flex; }
  .stat { flex: 1; text-align: center; color: var(--white); position: relative; }
  .stat + .stat::before { content: ""; position: absolute; left: 0; top: 2px; width: 3px; height: 70px;
    background: var(--white); border-radius: 2px; }
  .stat-value { font-family: "Archivo Black", sans-serif; font-size: 40px; line-height: 42px; }
  .stat-value small { font-family: "Roboto", sans-serif; font-size: 17px; font-weight: 400; }
  .stat-label { font-size: 20px; line-height: 26px; }

  .blend { position: absolute; left: 0; top: 777px; width: 100%; text-align: center;
    color: var(--white); font-size: 20.5px; line-height: 25px; font-weight: 400; }

  .badges { position: absolute; left: 83px; top: 838px; display: flex; gap: 24px; align-items: center; }
  .net-weight { position: absolute; right: 62px; top: 861px; color: var(--white); font-size: 18px; font-weight: 500; }
</style>
</head>
<body>
<main class="label">
  <div class="band-top" role="img" aria-label="Sand-coloured ornamental lace pattern background"></div>
  <div class="band-mid"></div>
  <div class="band-low" role="img" aria-label="Red background with drawn cocoa pod and flower line art"></div>

  <h1 class="wordmark">qu4cocoa</h1>
  <p class="product-name">Moon Tonic Batch 3</p>
  <p class="maker">fieldmark treats</p>

  <div class="hero-art" role="img" aria-label="Tattoo-style illustration in red and silver of a serpent coiled around a heart framed by roses"></div>

  <div class="crafted">
    <span class="crafted-rule left"></span>
    <span class="crafted-word">Handcrafted</span>
    <span class="crafted-rule right"></span>
  </div>
  <p class="descriptor">high protein milk chocolate bar<br>no sugar added</p>

  <div class="stats">
    <div class="stat"><div class="stat-value">13<small>g</small></div><div class="stat-label">protein</div></div>
    <div class="stat"><div class="stat-value">3<small>g</small></div><div class="stat-label">sugar</div></div>
    <div class="stat"><div class="stat-value">8<small>g</small></div><div class="stat-label">net carbs</div></div>
    <div class="stat"><div class="stat-value">10<small>g</small></div><div class="stat-label">fiber</div></div>
  </div>

  <p class="blend">67% organic cocoa, blended with milk<br>protein &amp; protein crisp</p>

  <div class="badges">
    <svg width="44" height="44" viewBox="0 0 44 44" aria-hidden="true"><circle cx="22" cy="22" r="20" fill="none" stroke="#c9a9a0" stroke-width="1.5"/></svg>
    <svg width="40" height="40" viewBox="0 0 40 40" aria-hidden="true"><rect x="6" y="6" width="28" height="28" fill="none" stroke="#ffffff" stroke-width="2"/></svg>
    <svg width="40" height="40" viewBox="0 0 40 40" aria-hidden="true"><circle cx="20" cy="20" r="16" fill="none" stroke="#ffffff" stroke-width="3"/></svg>
  </div>
  <p class="net-weight">1.9 oz (55g)</p>

  <div class="trim-guide"></div>
</main>
</body>
</html>
```